Poster Required for Cafe to promote coffee/staff discounts

Need an A3 size poster designed for our business to promote that we roast our own coffee, and that we offer discounts for staff.
I have attached a poster which we use to promote catering that our business offers, also have attached logos and our business card..
Also, I have attached our business card I would like the poster to look a little like that.
Eg. Our logo.
Then Specialty Coffee Roasters (under or next to this, in small print: Producing Slow Roasted Coffee)
Location
Download our App
Website
I would like the poster to state:
Tallowmere Health Staff receive $1 off their coffee or hot drink when presenting their staff pass.
Please don't hesitate to ask if you need more info.

```html
<!DOCTYPE html>
<html lang="en">
<head>
<meta charset="utf-8">
<title>Ward Roast – Slow Roasted Coffee Poster</title>
<link rel="stylesheet" href="https://fonts.googleapis.com/css2?family=Josefin+Sans:wght@300&family=Roboto:wght@300&family=Oswald:wght@700&family=Lobster&display=swap">
<style>
  :root {
    --backdrop: #3c3c3c;
    --espresso: #2a211d;
    --roast-deep: #2b1a10;
    --roast-mid: #7a4a26;
    --roast-glow: #d89a55;
    --crema: #f3d6a8;
    --text-light: #f4eee6;
    --button-text: #f6eaa2;
    --band: rgba(20, 12, 8, 0.82);
  }
  * { margin: 0; padding: 0; box-sizing: border-box; }
  html, body {
    width: 935px;
    height: 1200px;
    overflow: hidden;
    background: var(--backdrop);
  }
  .poster {
    position: absolute;
    left: 71px;
    top: 40px;
    width: 792px;
    height: 1120px;
    overflow: hidden;
    color: var(--text-light);
    font-family: "Roboto", Arial, sans-serif;
    font-weight: 300;
    text-align: center;
  }
  .poster__photo {
    position: absolute;
    inset: 0;
    background:
      radial-gradient(ellipse 45% 30% at 72% 55%, rgba(243, 214, 168, 0.55), transparent 70%),
      radial-gradient(ellipse 40% 55% at 92% 25%, rgba(216, 154, 85, 0.7), transparent 70%),
      radial-gradient(ellipse 70% 50% at 30% 62%, rgba(122, 74, 38, 0.9), transparent 75%),
      linear-gradient(160deg, var(--roast-mid) 0%, var(--roast-deep) 55%, #1a0f09 100%);
  }
  .brand {
    position: absolute;
    left: 206px;
    top: 30px;
    width: 380px;
    height: 380px;
    border-radius: 50%;
    background: var(--espresso);
    display: flex;
    flex-direction: column;
    justify-content: center;
    align-items: center;
  }
  .brand__name {
    font-family: "Josefin Sans", Arial, sans-serif;
    font-weight: 300;
    font-size: 50px;
    line-height: 1.15;
    letter-spacing: 5px;
    color: var(--text-light);
  }
  .tagline {
    position: absolute;
    top: 444px;
    width: 100%;
    font-size: 19px;
  }
  .location {
    position: absolute;
    top: 604px;
    width: 100%;
    font-size: 29px;
    line-height: 40px;
  }
  .app-button {
    position: absolute;
    left: 243px;
    top: 795px;
    width: 307px;
    height: 50px;
    border-radius: 25px;
    background: #120b07;
    border: 1px solid #5a4a3a;
    font-family: "Oswald", Impact, sans-serif;
    font-weight: 700;
    font-size: 28px;
    line-height: 48px;
    letter-spacing: 0.5px;
    color: var(--button-text);
  }
  .website {
    position: absolute;
    top: 876px;
    width: 100%;
    font-size: 25px;
    color: #e8ddd2;
  }
  .offer-band {
    position: absolute;
    left: 0;
    top: 947px;
    width: 100%;
    height: 113px;
    background: var(--band);
    display: flex;
    align-items: center;
    justify-content: center;
  }
  .offer-band__text {
    font-family: "Lobster", cursive;
    font-size: 25px;
    line-height: 39px;
    color: var(--button-text);
    letter-spacing: 0.5px;
  }
</style>
</head>
<body>
  <main class="poster">
    <div class="poster__photo" role="img" aria-label="Close-up photograph of a steaming cup of coffee with roasted beans in warm light"></div>

    <div class="brand">
      <p class="brand__name">WARD<br>ROAST</p>
    </div>

    <p class="tagline">Producing Slow Roasted Coffee</p>

    <p class="location">Located at Redgum Hospital<br>QUEENSLAND, AUSTRALIA</p>

    <p class="app-button">DOWNLOAD OUR APP</p>

    <p class="website">wardroast.com.au</p>

    <div class="offer-band">
      <p class="offer-band__text">Tallowmere Health Staff receive $1 off their Coffee or<br>Hot Drink when presenting their Staff Pass.</p>
    </div>
  </main>
</body>
</html>
```